Webdesign für Herstellung von Geschenk- und Dekorationsartikeln
Kobalt Prismo ist ein sehr angenehmer und professioneller Designer, der sich viele Gedanken über mein Projekt gemacht hat und ein Design, passend zu meinen Artikeln entworfen hat. Neben einer kompetenten Beratung gab es viele hilfreiche Vorschläge, die über den eigentlichen Auftrag hinaus gingen. Der Designer ist sehr zu empfehlen. Vielen Dank für den freundlichen Kontakt!
Zielgruppe
Wir sind eine kleine Firma, die mit einem Lasergravierer Geschenk- und Dekorationsartikel herstellt, verziert und beschriftet. Hierzu wird hauptsächlich Holz, Papier, Kork, Filz und Glas als Material eingesetzt.
Auch Schmuck , wie z.B. Kettenanhänger und Ohrringe aus Holz werden gefertigt.
Außerdem werden Fotogravur-Arbeiten nach Kundenwunsch angeboten.
Haupt-Zielgruppe sind Frauen ab 30.
Aufgabenstellung
Das Design soll etwas verspielt sein und Freude an den kleinen Dingen des Lebens ausdrücken. Es soll nicht zu sachlich und kühl sein.
Das vorhandene Logo wird bereit gestellt.
Es existiert noch keine Webseite. Die zukünftige Webseite soll über einen Shop verfügen.
Von der Shop-Darstellung her, hat mir die Webseite 'www.qvhauswerk.ch' gefallen.
Es wäre gut, wenn die im Logo vorhandenen Farben auch auf dem Design für die Webseite auftauchen würden.
Als Design-Tool wäre Adobe Photoshop (PSD) für die Erstellung gut.

```html
<!DOCTYPE html>
<html lang="de">
<head>
<meta charset="utf-8">
<title>Lumora Laserdeko – Produkte</title>
<link href="https://fonts.googleapis.com/css2?family=Fira+Sans:wght@400;500;600&family=Great+Vibes&display=swap" rel="stylesheet">
<style>
:root{
  --gold:#b0843e;
  --gold-soft:#c29a5c;
  --cream:#f3e9e0;
  --chip:#f2e5d8;
  --text:#5b5754;
  --muted:#a9a4a0;
  --line:#ece4dc;
  --white:#ffffff;
}
*{margin:0;padding:0;box-sizing:border-box}
html,body{width:924px;height:1200px;overflow:hidden;background:var(--white)}
body{position:relative;font-family:"Fira Sans",sans-serif;color:var(--text)}
a{color:inherit;text-decoration:none}

.site-header{position:absolute;left:0;top:0;width:924px;height:136px;background:var(--cream)}
.brand{position:absolute;left:104px;top:52px;display:flex;align-items:center;gap:6px;color:var(--text);font-family:"Fira Sans",sans-serif;font-size:26px;font-weight:400;letter-spacing:.5px}
.brand-dot{width:12px;height:12px;border-radius:50%;border:1.5px solid var(--gold)}
.main-nav{position:absolute;top:66px;left:0;font-size:10px;letter-spacing:.4px;color:var(--gold)}
.main-nav a{position:absolute;white-space:nowrap}
.header-icons{position:absolute;top:66px;left:755px;display:flex;gap:12px}
.header-icons svg{width:15px;height:15px;stroke:var(--gold);fill:none;stroke-width:2}

.breadcrumb{position:absolute;left:104px;top:146px;font-size:8.5px;font-weight:500}
.breadcrumb span{color:var(--gold)}
.divider{position:absolute;left:0;top:166px;width:924px;height:1px;background:var(--line)}

.intro{position:absolute;left:104px;top:184px;width:720px}
.intro h1{font-size:12.5px;font-weight:500;color:var(--gold);margin-bottom:8px}
.intro p{font-size:8.4px;line-height:11.4px;font-weight:500;color:var(--text)}

.filter-box{position:absolute;left:104px;top:297px;width:196px;height:254px;border:1px solid var(--gold-soft);border-radius:14px}
.filter-label{position:absolute;left:19px;font-size:9.5px;font-weight:500}
.chev{position:absolute;left:168px;width:8px;height:8px}
.chev path{stroke:var(--muted);fill:none;stroke-width:1.5}
.range-row{position:absolute;left:19px;top:47px;font-size:8.5px;font-weight:500}
.range-input{position:absolute;top:-4px;width:44px;height:16px;border-radius:8px;background:var(--chip);font-size:7.5px;color:var(--gold);padding:3px 0 0 8px}
.slider-track{position:absolute;left:20px;top:176px;width:156px;height:2px;background:var(--line)}
.slider{position:absolute;left:20px;top:79px;width:156px;height:2px;background:var(--line)}
.slider-fill{position:absolute;left:21px;top:0;width:71px;height:2px;background:var(--gold)}
.slider-knob{position:absolute;top:-2.5px;width:7px;height:7px;border-radius:50%;background:var(--gold)}
.cat-list{position:absolute;left:19px;top:136px;list-style:none;font-size:8.3px;font-weight:500}
.cat-list li{display:flex;align-items:center;gap:9px;height:20px}
.cat-list li i{width:8px;height:8px;border-radius:50%;background:#eceaeb}
.apply-btn{position:absolute;left:45px;top:214px;width:102px;height:25px;border-radius:13px;background:var(--gold);color:var(--white);font-size:9.5px;font-weight:500;text-align:center;line-height:25px;box-shadow:2px 2px 3px rgba(0,0,0,.12)}

.active-chip{position:absolute;top:297px;height:20px;border-radius:10px;font-size:8.5px;font-weight:500;color:var(--gold);line-height:20px}
.chip-glas{left:328px;width:80px;background:var(--chip);padding-left:10px}
.chip-glas b{position:absolute;right:8px;font-weight:500}
.chip-reset{left:417px;width:81px;border:1px solid var(--gold-soft);text-align:center;line-height:18px}
.sort{position:absolute;left:703px;top:302px;font-size:8px;color:var(--muted)}
.view-toggle{position:absolute;left:782px;top:300px;display:flex;gap:8px}
.view-toggle svg{width:13px;height:12px}

.product-grid{position:absolute;left:328px;top:324px;display:grid;grid-template-columns:repeat(3,147px);column-gap:23px;row-gap:0}
.product-card{height:226px}
.product-media{width:147px;height:147px}
.media-sign{background:linear-gradient(#d9d5d6,#d9d5d6);padding:9px 13px;}
.media-sign div{width:100%;height:100%;background:#8e8f99;border:2px solid #e8d9d3}
.media-cork{background:var(--white);border:1px solid #eee6e2;padding:10px}
.media-cork div{width:100%;height:100%;border-radius:6px;background:radial-gradient(circle at 50% 45%,#b08462,#8f6a4e);box-shadow:1px 2px 3px rgba(0,0,0,.25)}
.media-wood{background:linear-gradient(135deg,#ddd8cf,#cbc4b8)}
.product-title{margin-top:7px;padding-left:2px;font-size:10.5px;color:var(--gold-soft)}
.product-desc{padding-left:2px;font-size:8px;line-height:10px;color:var(--text)}
.product-price{padding-left:2px;margin-top:6px;font-size:11px;font-weight:600;color:var(--gold)}

.pagination{position:absolute;left:487px;top:1004px;display:flex;gap:6px}
.pagination span{width:17px;height:17px;border-radius:50%;background:var(--gold);color:var(--white);font-size:8.5px;font-weight:600;text-align:center;line-height:17px}
.pagination .current{background:var(--chip);color:var(--gold)}
.pagination svg{width:9px;height:9px;margin-top:4px}

.site-footer{position:absolute;left:0;top:1050px;width:924px;height:150px}
.footer-brand{position:absolute;left:104px;top:18px;display:flex;align-items:center;gap:5px;font-size:22px;color:var(--text)}
.footer-col{position:absolute;top:2px;display:flex;gap:13px}
.footer-col h4{font-size:7px;font-weight:600;letter-spacing:.3px;color:var(--gold)}
.footer-col ul{list-style:none;font-size:5.8px;line-height:7.8px;color:var(--gold);padding-top:2px}
.social{position:absolute;left:776px;top:4px;display:flex;gap:9px}
.social i{width:8px;height:8px;border-radius:50%;background:var(--gold)}
</style>
</head>
<body>

<header class="site-header">
  <div class="brand"><span class="brand-dot"></span>Lumora</div>
  <nav class="main-nav">
    <a style="left:397px">HOME</a>
    <a style="left:447px">ÜBER UNS</a>
    <a style="left:520px">PRODUKTE</a>
    <a style="left:599px">BLOG</a>
    <a style="left:650px">KONTAKT</a>
  </nav>
  <div class="header-icons">
    <svg viewBox="0 0 16 16"><circle cx="6.5" cy="6.5" r="4.5"/><path d="M10 10l4.5 4.5"/></svg>
    <svg viewBox="0 0 16 16" style="stroke-width:1.5"><circle cx="8" cy="5" r="3.2"/><path d="M2.5 15c0-3.5 2.5-5 5.5-5s5.5 1.5 5.5 5z"/></svg>
    <svg viewBox="0 0 16 16" style="stroke-width:1.6"><path d="M1 2h2.5l2 8.5h8l1.5-6H4.5"/><circle cx="6.5" cy="13.5" r="1"/><circle cx="12.5" cy="13.5" r="1"/></svg>
  </div>
</header>

<div class="breadcrumb">Home &gt; <span>Produkte</span></div>
<div class="divider"></div>

<section class="intro">
  <h1>Durchstöbern Sie unser breites Produktspektrum</h1>
  <p>Lorem ipsum dolor sit amet, consectetuer adipiscing elit. Aenean commodo ligula eget dolor. Aenean massa. Cum sociis natoque penatibus et magnis dis parturient montes, nascetur ridiculus mus. Donec quam felis, ultricies nec, pellentesque eu, pretium quis, sem. Nulla consequat massa quis enim. Donec pede justo, fringilla vel, aliquet nec, vulputate eget, arcu. In enim justo, rhoncus ut, imperdiet a, venenatis vitae, justo. Nullam dictum felis eu pede mollis pretium. Integer tincidunt. Cras dapibus.<br>Vivamus elementum semper nisi. Aenean vulputate eleifend tellus. Aenean leo ligula, porttitor eu, consequat vitae, eleifend ac, enim.</p>
</section>

<aside class="filter-box">
  <div class="filter-label" style="top:18px">Filter</div>
  <svg class="chev" style="top:22px" viewBox="0 0 8 8"><path d="M1 6l3-3 3 3"/></svg>
  <div class="range-row">von
    <span class="range-input" style="left:22px">5€</span>
    <span style="position:absolute;left:97px">bis</span>
    <span class="range-input" style="left:115px">80€</span>
  </div>
  <div class="slider">
    <div class="slider-fill"></div>
    <span class="slider-knob" style="left:19px"></span>
    <span class="slider-knob" style="left:89px"></span>
  </div>
  <div class="filter-label" style="top:116px">Kategorien</div>
  <svg class="chev" style="top:120px" viewBox="0 0 8 8"><path d="M1 6l3-3 3 3"/></svg>
  <ul class="cat-list">
    <li><i></i>Gravuren</li>
    <li><i></i>Holz</li>
    <li><i></i>Glas</li>
  </ul>
  <a class="apply-btn">Filter anwenden</a>
</aside>

<div class="active-chip chip-glas">Glas<b>x</b></div>
<div class="active-chip chip-reset">zurücksetzen</div>
<div class="sort">beliebteste &nbsp;&nbsp;&nbsp;⌄</div>
<div class="view-toggle">
  <svg viewBox="0 0 13 12" fill="#b0843e"><rect x="0" y="0" width="3.5" height="3.2"/><rect x="4.7" y="0" width="3.5" height="3.2"/><rect x="9.4" y="0" width="3.5" height="3.2"/><rect x="0" y="4.4" width="3.5" height="3.2"/><rect x="4.7" y="4.4" width="3.5" height="3.2"/><rect x="9.4" y="4.4" width="3.5" height="3.2"/><rect x="0" y="8.8" width="3.5" height="3.2"/><rect x="4.7" y="8.8" width="3.5" height="3.2"/><rect x="9.4" y="8.8" width="3.5" height="3.2"/></svg>
  <svg viewBox="0 0 13 12" fill="#b8b4b1"><rect y="0" width="13" height="2.5"/><rect y="4.7" width="13" height="2.5"/><rect y="9.4" width="13" height="2.5"/></svg>
</div>

<main class="product-grid">
  <article class="product-card"><div class="product-media media-sign" role="img" aria-label="Gerahmtes Bild mit handgeschriebenem Spruch"><div></div></div><h3 class="product-title">Personalisierte Bilder</h3><p class="product-desc">personalisierte Bilder als Geschenk zum Geburtstag ihrer Freunde</p><p class="product-price">3.33€</p></article>
  <article class="product-card"><div class="product-media media-cork" role="img" aria-label="Gravierter Korkuntersetzer mit Spruch"><div></div></div><h3 class="product-title">Personalisierte Bilder</h3><p class="product-desc">personalisierte Bilder als Geschenk zum Geburtstag ihrer Freunde</p><p class="product-price">3.33€</p></article>
  <article class="product-card"><div class="product-media media-wood" role="img" aria-label="Holzbrett mit gravierter Figur"></div><h3 class="product-title">Personalisierte Bilder</h3><p class="product-desc">personalisierte Bilder als Geschenk zum Geburtstag ihrer Freunde</p><p class="product-price">3.33€</p></article>
  <article class="product-card"><div class="product-media media-sign" role="img" aria-label="Gerahmtes Bild mit handgeschriebenem Spruch"><div></div></div><h3 class="product-title">Personalisierte Bilder</h3><p class="product-desc">personalisierte Bilder als Geschenk zum Geburtstag ihrer Freunde</p><p class="product-price">3.33€</p></article>
  <article class="product-card"><div class="product-media media-cork" role="img" aria-label="Gravierter Korkuntersetzer mit Spruch"><div></div></div><h3 class="product-title">Personalisierte Bilder</h3><p class="product-desc">personalisierte Bilder als Geschenk zum Geburtstag ihrer Freunde</p><p class="product-price">3.33€</p></article>
  <article class="product-card"><div class="product-media media-wood" role="img" aria-label="Holzbrett mit gravierter Figur"></div><h3 class="product-title">Personalisierte Bilder</h3><p class="product-desc">personalisierte Bilder als Geschenk zum Geburtstag ihrer Freunde</p><p class="product-price">3.33€</p></article>
  <article class="product-card"><div class="product-media media-sign" role="img" aria-label="Gerahmtes Bild mit handgeschriebenem Spruch"><div></div></div><h3 class="product-title">Personalisierte Bilder</h3><p class="product-desc">personalisierte Bilder als Geschenk zum Geburtstag ihrer Freunde</p><p class="product-price">3.33€</p></article>
  <article class="product-card"><div class="product-media media-cork" role="img" aria-label="Gravierter Korkuntersetzer mit Spruch"><div></div></div><h3 class="product-title">Personalisierte Bilder</h3><p class="product-desc">personalisierte Bilder als Geschenk zum Geburtstag ihrer Freunde</p><p class="product-price">3.33€</p></article>
  <article class="product-card"><div class="product-media media-wood" role="img" aria-label="Holzbrett mit gravierter Figur"></div><h3 class="product-title">Personalisierte Bilder</h3><p class="product-desc">personalisierte Bilder als Geschenk zum Geburtstag ihrer Freunde</p><p class="product-price">3.33€</p></article>
</main>

<nav class="pagination">
  <span class="current">1</span><span>2</span><span>3</span>
  <span><svg viewBox="0 0 9 9"><path d="M3 1.5l3 3-3 3" stroke="#fff" stroke-width="1.8" fill="none"/></svg></span>
</nav>

<footer class="site-footer">
  <div class="footer-brand"><span class="brand-dot"></span>Lumora</div>
  <div class="footer-col" style="left:267px">
    <h4>SITEMAP</h4>
    <ul><li>Kontakt</li><li>Über Uns</li><li>Verpackung &amp; Versand</li><li>FAQ</li><li>Rücksendungen</li><li>Produkte</li></ul>
  </div>
  <div class="footer-col" style="left:421px">
    <h4>INFORMATIONEN</h4>
    <ul><li>AGB</li><li>Datenschutz</li><li>Impressum</li></ul>
  </div>
  <div class="social"><i></i><i></i><i></i></div>
</footer>

</body>
</html>
```